Company Profile for Consulting Comany

Need Company profile to be designed in a professional way.

for inspiring :-
https://www.vimolia.net/gallery/5307462/COMPANY-PROFILE
https://www.vimolia.net/gallery/20934617/Biotech-Product-Catalog-No1-(Laminar-Air-Flow)
https://www.vimolia.net/gallery/38720954/RKT-Tramvale-Company-Profile-2014-(RKT-Rebrand-part-2)

Target Market(s)

Corporate

Industry/Entity Type

It Company

Font styles to use
Sans Serif

Requirements
Must have
• Landscape A4 size
• Must go with the logo branding
• Must Have Visual Identity is the most important
• Must Have mpty spaces

```html
<!DOCTYPE html>
<html lang="en">
<head>
<meta charset="utf-8">
<title>Pivot Works – Company Profile</title>
<link rel="stylesheet" href="https://fonts.googleapis.com/css2?family=Raleway:wght@300;400;600;800&display=swap">
<style>
  :root{
    --backdrop:#e4e4e4;
    --ink-black:#0b0c0d;
    --charcoal:#1b1d1f;
    --teal:#3a9fc1;
    --teal-soft:rgba(58,159,193,.55);
    --navy:#0f1f5a;
    --navy-deep:#0a1540;
    --paper:#ffffff;
    --text-grey:#4a4a4a;
    --rule:#9a9a9a;
  }
  *{box-sizing:border-box;margin:0;padding:0}
  html,body{width:1200px;height:880px;overflow:hidden}
  body{background:var(--backdrop);font-family:"Raleway",sans-serif;position:relative}

  .page{position:absolute;width:560px;height:396px;overflow:hidden;box-shadow:0 6px 18px rgba(0,0,0,.18)}

  /* ---------- Cover ---------- */
  .cover{left:320px;top:28px;background:var(--ink-black)}
  .cover-photo{position:absolute;left:0;top:70px;width:560px;height:250px;
    background:linear-gradient(180deg,#3b3d40 0%,#6d6f72 45%,#2b2c2e 100%)}
  .cover-stripe{position:absolute;left:455px;top:70px;width:70px;height:170px;background:var(--teal-soft)}
  .cover-brand{position:absolute;left:22px;top:40px;width:118px;height:92px;background:var(--charcoal);
    display:flex;align-items:center;justify-content:center;gap:7px}
  .brand-mark{width:10px;height:10px;background:var(--teal)}
  .brand-name{color:var(--teal);font-weight:800;font-size:15px;line-height:1.05;text-align:left}
  .cover-tagline{position:absolute;left:40px;bottom:20px;color:var(--teal);line-height:1}
  .cover-tagline .lead{display:block;font-weight:300;font-size:26px;letter-spacing:.5px}
  .cover-tagline .strong{display:block;font-weight:800;font-size:27px;margin-top:3px}

  /* ---------- Spread ---------- */
  .spread-left{left:40px;top:456px;background:var(--paper);padding:26px 30px 0 30px}
  .spread-right{left:600px;top:456px;background:var(--navy);overflow:visible}

  .section{margin-bottom:10px}
  .section-title{color:var(--teal);font-weight:400;font-size:13px;letter-spacing:.5px;
    border-bottom:1px solid var(--rule);padding-bottom:1px;margin-bottom:4px}
  .section p,.section li{color:var(--text-grey);font-size:7.2px;line-height:1.4}
  .section ul{list-style:none}
  .section li{padding-left:9px;position:relative}
  .section li::before{content:"";position:absolute;left:0;top:2.5px;width:4px;height:4px;border-radius:50%;background:var(--teal)}
  .value{margin-bottom:5px}
  .value-name{color:var(--teal);font-size:6.8px;text-transform:uppercase;letter-spacing:.3px}

  .right-photo{position:absolute;left:0;top:0;width:560px;height:180px;
    background:linear-gradient(180deg,#1a2f8a 0%,#16267a 55%,#0a1438 100%)}
  .who-band{position:absolute;left:-28px;top:170px;width:588px;height:40px;background:var(--teal);
    display:flex;align-items:center;padding-left:68px}
  .who-band h2{color:#fff;font-weight:400;font-size:19px;letter-spacing:.5px}
  .summary{position:absolute;left:40px;top:226px;width:400px}
  .summary h3{color:var(--teal);font-weight:400;font-size:13px;letter-spacing:.5px;margin-bottom:5px}
  .summary p{color:#fff;font-weight:600;font-size:7.4px;line-height:1.45}
</style>
</head>
<body>

<section class="page cover">
  <div class="cover-photo" role="img" aria-label="Black and white photograph of tall tree trunks in a misty forest"></div>
  <div class="cover-stripe"></div>
  <div class="cover-brand">
    <span class="brand-mark"></span>
    <span class="brand-name">Pivot<br>Works</span>
  </div>
  <h1 class="cover-tagline">
    <span class="lead">WE CAN HELP YOU TO</span>
    <span class="strong">MAKE CHANGE HAPPEN</span>
  </h1>
</section>

<section class="page spread-left">
  <div class="section">
    <h2 class="section-title">VISION</h2>
    <p>"To become the leading HR outsourcing company in the Middle East and stand known of quality services."</p>
  </div>
  <div class="section">
    <h2 class="section-title">MISSION</h2>
    <p>We have a multi-layered mission statement catering for the needs of our customers in addition to increasing the value of our services and upgrading our standing among our competitors. Our missions are:</p>
    <ul>
      <li>To provide convenient HR solutions to SMEs so they can focus on the core of their business.</li>
      <li>To play our role in economic development of Saudi Arabia and other Middle East countries.</li>
      <li>To develop a professional relationship with our valued clientele and investors.</li>
      <li>To bring innovation in HR services through technology.</li>
    </ul>
  </div>
  <div class="section">
    <h2 class="section-title">VALUES</h2>
    <div class="value"><div class="value-name">Integrity</div><p>Pivot Works will ensure integrity within employees and with clients, investors and strategic partners.</p></div>
    <div class="value"><div class="value-name">Workplace Entertainment</div><p>Pivot Works will provide enjoyment of all employees at the workplace to promote work as a passion instead of a profession.</p></div>
    <div class="value"><div class="value-name">Accountability</div><p>In Pivot Works, from MD to staff everyone will be accountable for their actions and decision.</p></div>
    <div class="value"><div class="value-name">Pursuit of Excellence</div><p>Each employee and stakeholder will strive for excellence in his role and professional activities.</p></div>
    <div class="value"><div class="value-name">Quality Control</div><p>Pivot Works will implement strict quality control to improve the standard of its services continuously.</p></div>
    <div class="value"><div class="value-name">Affordability</div><p>Services of Pivot Works will be affordable to meet the demands of local companies.</p></div>
  </div>
</section>

<section class="page spread-right">
  <div class="right-photo" role="img" aria-label="Night photograph of a coastal city skyline with a tall sail-shaped hotel tower lit in blue"></div>
  <div class="who-band"><h2>WHO WE ARE?</h2></div>
  <div class="summary">
    <h3>EXECUTIVE SUMMARY</h3>
    <p>Pivot Works is professional HR &amp; OD Organization, which is Specialized in Talent and Organizational Development, Career Coaching, Leadership Assessment and Development, Total Reward, HR Technology &amp; providing a wide range of outsourcing payroll and recruitment services with a vision to be the leading HR outsourcing company in the Middle East. Pivot Works is a local house of HR &amp; OD expertise with global experience, driven by one thought, to raise the bar of local HR practices and knowledge. Pivot Works have developed partnerships with various companies and organizations, among those Corvantis will be the strategic partner to provide HR outsourcing services through their platforms.</p>
  </div>
</section>

</body>
</html>
```